Business Card Design

I need a business card design for a new company based in Sydney called 'The Brisk Ladle'. We deliver organic, gourmet and fine foods to your door.

I would like to see creative, unique designs which use colours which represent health and nature like green.

Target Market(s)

Health conscious 20 to 35 year olds.

Industry/Entity Type

Health

Contact Information for Business Card

The Brisk Ladle, Owen Pardalis, owen@thebriskladle.com.au, 0427865193

Requirements
Must have
• My logo.

```html
<!DOCTYPE html>
<html lang="en">
<head>
<meta charset="utf-8">
<title>The Brisk Ladle — Business Card</title>
<link rel="stylesheet" href="https://fonts.googleapis.com/css2?family=Open+Sans:wght@300;400;700&display=swap">
<style>
  :root {
    --page-bg: #e9e7e4;
    --card-bg: #ffffff;
    --green-dark: #3f8a3c;
    --green-mid: #5a9e55;
    --green-light: #9ccc3c;
    --green-pale: #b9dd6a;
    --ink: #2b2b2b;
    --shadow: rgba(0, 0, 0, 0.18);
  }
  * { box-sizing: border-box; margin: 0; padding: 0; }
  html, body {
    width: 1200px; height: 800px; overflow: hidden;
    background: var(--page-bg);
    font-family: "Open Sans", Arial, sans-serif;
  }
  .canvas { position: relative; width: 1200px; height: 800px; }

  .card {
    position: absolute;
    background: var(--card-bg);
    box-shadow: 0 6px 18px var(--shadow);
    overflow: hidden;
  }

  /* Back of card: portrait, name set vertically */
  .card-back {
    left: 110px; top: 140px;
    width: 300px; height: 520px;
  }
  .card-back .wordmark {
    position: absolute;
    left: 50%; top: 50%;
    transform: translate(-50%, -50%) rotate(90deg);
    white-space: nowrap;
    font-weight: 300;
    font-size: 62px;
    letter-spacing: 1px;
    color: var(--green-light);
    display: flex; align-items: center; gap: 18px;
  }
  .card-back .mark-dot {
    width: 40px; height: 40px; border-radius: 50%;
    background: var(--green-mid);
  }

  /* Front of card: landscape */
  .card-front {
    left: 500px; top: 240px;
    width: 590px; height: 338px;
  }
  .brand {
    position: absolute; left: 180px; top: 26px;
    display: flex; align-items: center; gap: 12px;
  }
  .brand .mark-dot {
    width: 44px; height: 44px; border-radius: 50%;
    background: var(--green-light);
  }
  .brand .brand-name {
    font-weight: 300; font-size: 34px; color: var(--green-mid);
    white-space: nowrap;
  }
  .name-band {
    position: absolute; left: 0; top: 98px;
    width: 100%; height: 50px;
    background: linear-gradient(90deg, var(--green-mid), var(--green-dark));
    padding: 6px 0 0 26px;
  }
  .name-band .person {
    font-weight: 700; font-size: 17px; letter-spacing: 0.5px;
    color: #fff; text-transform: uppercase; line-height: 1.2;
  }
  .name-band .role {
    font-size: 11px; color: var(--green-pale); line-height: 1.3;
  }
  .contact {
    position: absolute; left: 26px; top: 166px;
    list-style: none;
  }
  .contact li {
    display: flex; align-items: center; gap: 8px;
    font-size: 13px; color: var(--ink); line-height: 21px;
  }
  .contact svg { width: 12px; height: 12px; flex: none; }
</style>
</head>
<body>
<main class="canvas">

  <section class="card card-back" aria-label="Card back">
    <div class="wordmark"><span class="mark-dot"></span>The Brisk Ladle</div>
  </section>

  <section class="card card-front" aria-label="Card front">
    <div class="brand">
      <span class="mark-dot"></span>
      <span class="brand-name">The Brisk Ladle</span>
    </div>

    <div class="name-band">
      <p class="person">Owen Pardalis</p>
      <p class="role">Director</p>
    </div>

    <ul class="contact">
      <li>
        <svg viewBox="0 0 12 12" aria-hidden="true"><rect width="12" height="12" rx="2" fill="var(--green-mid)"/><rect x="4" y="2" width="4" height="8" rx="1" fill="#fff"/></svg>
        0427865193
      </li>
      <li>
        <svg viewBox="0 0 12 12" aria-hidden="true"><rect width="12" height="12" rx="2" fill="var(--green-mid)"/><path d="M2.5 4h7v4.5h-7z M2.5 4l3.5 2.5L9.5 4" fill="none" stroke="#fff" stroke-width="1"/></svg>
        owen@thebriskladle.com.au
      </li>
      <li>
        <svg viewBox="0 0 12 12" aria-hidden="true"><rect width="12" height="12" rx="2" fill="var(--green-mid)"/><circle cx="6" cy="6" r="3.3" fill="none" stroke="#fff" stroke-width="1"/><path d="M2.7 6h6.6M6 2.7v6.6" stroke="#fff" stroke-width="0.8"/></svg>
        www.thebriskladle.com.au
      </li>
    </ul>
  </section>

</main>
</body>
</html>
```